Professional Business Cards

We need a nice looking, profession and modern business card for our new company. Our logo is attatched

Target Market(s)

Young Professionals

Industry/Entity Type

Financial

Contact Information for Business Card

FRONT

Morvane Tally Pty Ltd
Level 22, Halden Court, 48 Wirrapool St
Sydney NSW 2000
ABN : 57 304 918 226

Derek Wallis - Chief Operations Officer
P : 02 7153 2819
M: 0418 395 207
derek@morvanetally,com

BACK

- Cryptocurrency Exchange Services
- Cryptocurrency Mining Operations
- Cryptocurrency Investment Fund Offering

Font styles to use
Sans Serif

Colors
0255a3
9d9d9d

```html
<!DOCTYPE html>
<html lang="en">
<head>
<meta charset="utf-8">
<title>Morvane Tally – Business Card</title>
<link rel="stylesheet" href="https://fonts.googleapis.com/css2?family=Roboto:wght@400;500;700&family=Roboto+Condensed:wght@700&display=swap">
<style>
  :root {
    --brand-blue: #0255a3;
    --brand-grey: #9d9d9d;
    --backdrop: #2b2b2b;
    --card-dark: #1f2022;
    --card-light: #f4f4f4;
    --ink: #4a4a4a;
    --ink-soft: #707070;
    --white: #ffffff;
  }
  * { margin: 0; padding: 0; box-sizing: border-box; }
  html, body { width: 1200px; height: 960px; overflow: hidden; }
  body {
    background: var(--backdrop);
    font-family: "Roboto", Arial, sans-serif;
    position: relative;
  }
  .card {
    position: absolute;
    left: 320px;
    width: 600px;
    height: 342px;
    box-shadow: 0 6px 18px rgba(0,0,0,.45);
  }
  .card--front { top: 100px; background: var(--card-dark); }
  .card--back { top: 493px; background: var(--card-light); }

  .abs { position: absolute; white-space: nowrap; }

  /* front */
  .brand-lockup {
    left: 0; right: 0; top: 150px;
    display: flex; justify-content: center; align-items: center; gap: 16px;
  }
  .brand-mark {
    width: 34px; height: 34px; background: var(--brand-blue);
  }
  .brand-name {
    font-weight: 700; font-size: 44px; letter-spacing: 2px;
    color: var(--brand-blue); line-height: 1;
  }
  .services {
    left: 0; right: 0; top: 282px; text-align: center;
    color: var(--white); font-size: 14.5px; line-height: 18px;
  }
  .services .sep { font-size: 11px; padding: 0 4px; vertical-align: 1px; }

  /* back */
  .card--back .brand-name {
    left: 0; right: 0; top: 35px; text-align: center; font-size: 40px;
  }
  .person {
    right: 314px; top: 136px; text-align: right;
  }
  .person__name {
    font-family: "Roboto Condensed", Arial, sans-serif;
    font-weight: 700; font-size: 23px; color: var(--brand-blue); line-height: 26px;
  }
  .person__role { font-size: 16px; color: var(--ink-soft); line-height: 20px; font-weight: 500; }
  .contact { list-style: none; margin-top: 8px; }
  .contact li {
    font-size: 14.5px; color: var(--ink); line-height: 19.5px;
    display: flex; justify-content: flex-end; align-items: center; gap: 8px;
  }
  .contact svg { width: 13px; height: 13px; fill: var(--brand-blue); }
  .divider {
    left: 313px; top: 129px; width: 1px; height: 126px; background: #c4c4c4;
  }
  .company { left: 336px; top: 144px; }
  .company__pin { position: absolute; left: -4px; top: 1px; width: 13px; height: 16px; fill: var(--brand-blue); }
  .company__lines { padding-left: 19px; font-size: 14.5px; color: var(--ink); line-height: 18px; }
  .company__name { font-weight: 500; }
  .company__abn { margin-top: 5px; margin-left: -1px; }
  .footer-mark {
    left: 50px; top: 296px; width: 26px; height: 26px; background: var(--brand-blue);
  }
  .footer-rule {
    left: 80px; top: 310px; width: 484px; height: 2px; background: var(--brand-blue);
  }
  .website {
    left: 0; right: 0; padding-left: 30px; top: 289px; text-align: center;
    font-size: 14px; font-weight: 700; letter-spacing: 5px; color: var(--ink);
  }
</style>
</head>
<body>

<section class="card card--front">
  <div class="abs brand-lockup">
    <span class="brand-mark"></span>
    <span class="brand-name">MORVANE TALLY</span>
  </div>
  <p class="abs services">
    Cryptocurrency Exchange Services<span class="sep">◆</span>Cryptocurrency Mining Operations<br>
    Cryptocurrency Investment Fund Offering
  </p>
</section>

<section class="card card--back">
  <div class="abs brand-name">MORVANE TALLY</div>

  <div class="abs person">
    <h1 class="person__name">DEREK WALLIS</h1>
    <p class="person__role">Chief Operations Officer</p>
    <ul class="contact">
      <li>02 7153 2819
        <svg viewBox="0 0 24 24"><path d="M6.6 10.8a15.2 15.2 0 0 0 6.6 6.6l2.2-2.2c.3-.3.7-.4 1-.2 1.1.4 2.3.6 3.6.6.6 0 1 .4 1 1V20c0 .6-.4 1-1 1A17 17 0 0 1 3 4c0-.6.4-1 1-1h3.5c.6 0 1 .4 1 1 0 1.3.2 2.5.6 3.6.1.3 0 .7-.2 1z"/></svg>
      </li>
      <li>0418 395 207
        <svg viewBox="0 0 24 24"><path d="M7 1h10a2 2 0 0 1 2 2v18a2 2 0 0 1-2 2H7a2 2 0 0 1-2-2V3a2 2 0 0 1 2-2zm0 3v14h10V4zm5 15.5a1 1 0 1 0 0 2 1 1 0 0 0 0-2z"/></svg>
      </li>
      <li>derek@morvanetally.com
        <svg viewBox="0 0 24 24"><path d="M2 5h20v14H2zm2 2v.5l8 5 8-5V7l-8 5z"/></svg>
      </li>
    </ul>
  </div>

  <div class="abs divider"></div>

  <div class="abs company">
    <svg class="company__pin" viewBox="0 0 24 30"><path d="M12 0a10 10 0 0 0-10 10c0 7.5 10 20 10 20s10-12.5 10-20A10 10 0 0 0 12 0zm0 14a4 4 0 1 1 0-8 4 4 0 0 1 0 8z"/></svg>
    <div class="company__lines">
      <p class="company__name">Morvane Tally Pty Ltd</p>
      <p>Level 22, Halden Court</p>
      <p>48 Wirrapool St</p>
      <p>Sydney NSW 2000</p>
    </div>
    <p class="company__lines company__abn" style="padding-left:0">ABN : 57 304 918 226</p>
  </div>

  <div class="abs footer-mark"></div>
  <div class="abs footer-rule"></div>
  <p class="abs website">www.MORVANE.com</p>
</section>

</body>
</html>
```